Financial Advisor Graphic to Explain Proprietary and Differentiating Investment Strategy

We need a graphic that visualizes how we build a portfolio based on factors of the underlying companies. We use 8 main factors to objectively build an investment porftolio. Our colors are blues, greys (see www.pltvexgroup.com). We are thinking either a venn diagram approach or an atom approach with the factors around the middle "Core Portfolio". This is what differentiates us from everyone in the industry. This will be the key to all of our marketing

Target Market(s)

High net worth investors

Industry/Entity Type

Financial Service

Font styles to use
Serif

Requirements
Must have
• Graphic must be elegant. It is for the financial industry. It should include the following factors (in no order) to build a "Core Portfolio"
• -Counter Cyclical Industries
• -Industry Rate of Recovery
• -Price To Book
• -Absolute Risk
• -Market Capitalization
• -Liquidity
• -Dividend Yield
• -Buy Back Yield
Nice to have
• We are thinking an atom approach or a venn diagram but we are open to new ideas. It must portray the idea that we OBJECTIVELY apply these factors to stock selection to build a core portfolio for our investors. For color pallets see www.pltvexgroup.com It can go beyond the greys and blues but should not be too loud or playful. It can be high tech as long as it portrays seriousness of the financial markets
Should not have
• Can not be playful.

```html
<!DOCTYPE html>
<html lang="en">
<head>
<meta charset="utf-8">
<title>Core Portfolio Factors</title>
<link rel="stylesheet" href="https://fonts.googleapis.com/css2?family=Carlito:ital,wght@1,700&display=swap">
<style>
  :root {
    --bg-center: #0c0c78;
    --bg-mid: #0a0a4a;
    --bg-edge: #0e0e22;
    --factor-top: #0a90fa;
    --factor-bottom: #0072d2;
    --core-top: #aaaaaa;
    --core-bottom: #8c8c8c;
    --arrow: #a9d8f5;
    --glow: #8c8cf0;
    --label: #ffffff;
  }
  html, body {
    margin: 0;
    padding: 0;
    width: 1200px;
    height: 1200px;
    overflow: hidden;
  }
  .canvas {
    position: relative;
    width: 1200px;
    height: 1200px;
    background: radial-gradient(circle at 50% 48%, var(--bg-center) 0%, var(--bg-mid) 45%, var(--bg-edge) 100%);
    font-family: "Carlito", "Calibri", sans-serif;
  }
  .diagram {
    position: absolute;
    inset: 0;
  }
  .label {
    position: absolute;
    transform: translate(-50%, -50%);
    text-align: center;
    color: var(--label);
    font-weight: 700;
    font-style: italic;
    font-size: 35px;
    line-height: 46px;
    white-space: nowrap;
    text-shadow: 2px 3px 3px rgba(0, 0, 0, 0.45);
  }
  .label--core {
    font-size: 48px;
    line-height: 60px;
    text-shadow: 2px 3px 4px rgba(0, 0, 0, 0.5);
  }
</style>
</head>
<body>
<main class="canvas">
  <svg class="diagram" width="1200" height="1200" viewBox="0 0 1200 1200" aria-hidden="true">
    <defs>
      <linearGradient id="factor-fill" x1="0" y1="0" x2="0" y2="1" gradientUnits="objectBoundingBox">
        <stop offset="0" stop-color="var(--factor-top)"/>
        <stop offset="1" stop-color="var(--factor-bottom)"/>
      </linearGradient>
      <radialGradient id="core-fill" cx="0.5" cy="0.4" r="0.6">
        <stop offset="0" stop-color="var(--core-top)"/>
        <stop offset="1" stop-color="var(--core-bottom)"/>
      </radialGradient>
      <filter id="halo" x="-30%" y="-30%" width="160%" height="160%">
        <feGaussianBlur in="SourceAlpha" stdDeviation="10" result="blur"/>
        <feFlood flood-color="#8c8cf0" flood-opacity="0.55"/>
        <feComposite in2="blur" operator="in" result="glow"/>
        <feMerge>
          <feMergeNode in="glow"/>
          <feMergeNode in="SourceGraphic"/>
        </feMerge>
      </filter>
      <g id="factor-tile">
        <rect x="-120.5" y="-120.5" width="241" height="241" rx="40" transform="rotate(45)" fill="url(#factor-fill)"/>
      </g>
      <path id="pointer" d="M -20 -14 L 20 -14 L 0 14 Z" fill="var(--arrow)" stroke="var(--arrow)" stroke-width="6" stroke-linejoin="round"/>
    </defs>

    <g class="factor-tiles" filter="url(#halo)">
      <use href="#factor-tile" x="600" y="220"/>
      <use href="#factor-tile" x="386" y="384"/>
      <use href="#factor-tile" x="816" y="384"/>
      <use href="#factor-tile" x="222" y="600"/>
      <use href="#factor-tile" x="980" y="600"/>
      <use href="#factor-tile" x="386" y="816"/>
      <use href="#factor-tile" x="816" y="816"/>
      <use href="#factor-tile" x="600" y="980"/>
    </g>

    <g class="core-tile" filter="url(#halo)">
      <rect x="458" y="458" width="284" height="284" rx="45" transform="rotate(45 600 600)" fill="url(#core-fill)"/>
    </g>

    <g class="pointers">
      <use href="#pointer" transform="translate(600 397)"/>
      <use href="#pointer" transform="translate(600 803) rotate(180)"/>
      <use href="#pointer" transform="translate(397 600) rotate(-90)"/>
      <use href="#pointer" transform="translate(803 600) rotate(90)"/>
      <use href="#pointer" transform="translate(482 482) rotate(-45)"/>
      <use href="#pointer" transform="translate(718 482) rotate(45)"/>
      <use href="#pointer" transform="translate(482 718) rotate(-135)"/>
      <use href="#pointer" transform="translate(718 718) rotate(135)"/>
    </g>
  </svg>

  <div class="label" style="left:603px; top:221px;">Counter<br>Cyclical<br>Industries</div>
  <div class="label" style="left:386px; top:386px;">Price<br>To Book</div>
  <div class="label" style="left:813px; top:390px;">Absolute<br>Risk</div>
  <div class="label" style="left:222px; top:598px;">Market<br>Capitalization</div>
  <div class="label" style="left:980px; top:607px;">Dividend<br>Yield</div>
  <div class="label" style="left:380px; top:818px;">Liquidity</div>
  <div class="label" style="left:813px; top:825px;">Buy Back<br>Yield</div>
  <div class="label" style="left:603px; top:981px;">Industry<br>Rate of<br>Recovery</div>
  <div class="label label--core" style="left:600px; top:596px;">Core<br>Portfolio</div>
</main>
</body>
</html>
```